An animal window cleaning business card

I want a business card design that includes a logo and tells people I am a WINDOW WASHING COMPANY right away.
Were based in Maine, we do window cleaning, pressure washing, and gutter cleaning. We like Pine trees, the Ocean, state of Maine symbols, Lobsters, Moose, Huskies, etc. My business name is "GLEAM HOUR PANES"
The card could also be designed to look like a gift credit card with a 50$ value.

Target Market(s)

my target audience is older folks with disposable money who live on the ocean or have secondary homes for vacation in Maine

Industry/Entity Type

Cleaning Services

Contact Information for Business Card

2.5x3" plastic if possible.

Font styles to use
Sans Serif

Requirements
Must have
• a symbol, or a logo that tells people I am a window washing company Instantly.
The words GLEAM HOUR, my phone number, my name, MY email
Nice to have
• a lobster holding a squeegee, or a stylized cartoonish version of a human huskie holding a squeegee,
Should not have
• a lighthouse
small hard to read text

```html
<!DOCTYPE html>
<html lang="en">
<head>
<meta charset="UTF-8">
<title>Gleam Hour Panes – Business Card</title>
<link rel="stylesheet" href="https://fonts.googleapis.com/css2?family=Poppins:wght@400;500;600;800&display=swap">
<style>
  :root {
    --page-bg: #e9edf2;
    --card-white: #ffffff;
    --brand-blue: #1a7bbd;
    --brand-navy: #173f73;
    --sky-light: #d9ecf8;
    --mascot-tone: #5b86b8;
    --text-white: #ffffff;
  }
  * { margin: 0; padding: 0; box-sizing: border-box; }
  html, body {
    width: 1200px;
    height: 900px;
    overflow: hidden;
    background: var(--page-bg);
    font-family: "Poppins", sans-serif;
  }
  .card {
    position: absolute;
    left: 100px;
    top: 163px;
    width: 1000px;
    height: 573px;
    border-radius: 30px;
    overflow: hidden;
    background: var(--card-white);
    box-shadow: 0 18px 40px rgba(23, 63, 115, 0.18);
  }
  .card-waves {
    position: absolute;
    inset: 0;
    width: 100%;
    height: 100%;
  }
  .mascot-area {
    position: absolute;
    left: 30px;
    top: 12px;
    width: 300px;
    height: 535px;
    border-radius: 40px;
    background: linear-gradient(180deg, var(--sky-light) 0%, var(--mascot-tone) 100%);
    opacity: 0.9;
  }
  .brand-name {
    position: absolute;
    left: 560px;
    top: 70px;
    width: 360px;
    display: flex;
    align-items: center;
    gap: 18px;
  }
  .brand-dot {
    flex: none;
    width: 40px;
    height: 40px;
    border-radius: 50%;
    background: var(--brand-blue);
  }
  .brand-text {
    font-weight: 800;
    font-size: 50px;
    line-height: 1.02;
    color: var(--brand-navy);
    letter-spacing: 1px;
  }
  .contact {
    position: absolute;
    left: 407px;
    top: 378px;
    color: var(--text-white);
  }
  .contact-name {
    font-weight: 600;
    font-size: 28px;
    letter-spacing: 0.5px;
    line-height: 1.2;
  }
  .contact-title {
    font-weight: 500;
    font-size: 22px;
    letter-spacing: 0.3px;
    line-height: 1.3;
    margin-bottom: 18px;
  }
  .contact-line {
    display: flex;
    align-items: center;
    gap: 10px;
    font-size: 21px;
    font-weight: 400;
    line-height: 1.45;
  }
  .contact-icon {
    width: 20px;
    height: 20px;
    flex: none;
  }
  .value-badge {
    position: absolute;
    left: 797px;
    top: 399px;
    width: 260px;
    height: 260px;
    border-radius: 50%;
    background: var(--brand-navy);
    border: 12px solid var(--card-white);
  }
  .value-amount {
    position: absolute;
    left: 878px;
    top: 494px;
    font-weight: 800;
    font-size: 50px;
    color: var(--text-white);
    letter-spacing: 1px;
    line-height: 1;
  }
</style>
</head>
<body>
  <main class="card">
    <svg class="card-waves" viewBox="0 0 1000 573" aria-hidden="true">
      <path d="M0,292 C200,272 360,352 560,342 C760,332 860,282 1000,256 L1000,573 L0,573 Z" fill="var(--brand-navy)"/>
      <path d="M0,308 C200,288 360,368 560,358 C760,348 860,298 1000,272 L1000,573 L0,573 Z" fill="var(--card-white)"/>
      <path d="M0,322 C200,306 360,386 560,376 C760,366 860,316 1000,290 L1000,573 L0,573 Z" fill="var(--brand-blue)"/>
    </svg>

    <div class="mascot-area" role="img" aria-label="Cartoon husky mascot in blue overalls holding a squeegee and a pressure washer wand"></div>

    <div class="brand-name">
      <span class="brand-dot"></span>
      <span class="brand-text">GLEAM HOUR<br>PANES</span>
    </div>

    <section class="contact">
      <p class="contact-name">ELLIS MARLOWE</p>
      <p class="contact-title">MANAGING DIRECTOR</p>
      <p class="contact-line">
        <svg class="contact-icon" viewBox="0 0 20 20" aria-hidden="true">
          <circle cx="10" cy="10" r="10" fill="var(--text-white)"/>
          <path d="M7 5.2l1.6 2.3-1 1.2a7 7 0 0 0 3.7 3.7l1.2-1 2.3 1.6-.7 1.7c-.3.5-.9.7-1.5.6A9 9 0 0 1 5 8.1c-.1-.6.1-1.2.6-1.5z" fill="var(--brand-blue)"/>
        </svg>
        207-555-0148
      </p>
      <p class="contact-line">
        <svg class="contact-icon" viewBox="0 0 20 20" aria-hidden="true">
          <circle cx="10" cy="10" r="10" fill="var(--text-white)"/>
          <rect x="5" y="6.5" width="10" height="7" rx="1" fill="var(--brand-blue)"/>
          <path d="M5.3 7l4.7 3.6L14.7 7" fill="none" stroke="var(--text-white)" stroke-width="1"/>
        </svg>
        ellis@gleamhourpanes.com
      </p>
    </section>

    <div class="value-badge"></div>
    <span class="value-amount">50$</span>
  </main>
</body>
</html>
```